Crimson Vantage Cleaning Solutions

Need a logo and business card design. I want to use a translucent business card. I want to abbreviate the name C.V.C.S. Commercial Cleaning, because my is Dov. I’d also like to incorporate a knight or something like that. I want the idea to tie in with the word Crimson. New ideas are welcome, i don’t want to limit anyone’s creativity.

Target Market(s)

Commercial Cleaning for businesses.

Contact Information for Business Card

Crimson
Vantage
Cleaning
Solutions

```html
<!DOCTYPE html>
<html lang="en">
<head>
<meta charset="utf-8">
<title>Crimson Vantage Cleaning Solutions — Business Card</title>
<link href="https://fonts.googleapis.com/css2?family=Work+Sans:wght@400;500;600&display=swap" rel="stylesheet">
<style>
  :root {
    --backdrop: #0d0d0d;
    --card: #1e1e1e;
    --card-edge: #262626;
    --ink: #ffffff;
    --ink-soft: #e6e6e6;
  }
  * { box-sizing: border-box; margin: 0; padding: 0; }
  html, body {
    width: 1200px; height: 900px; overflow: hidden;
    background: var(--backdrop);
    font-family: "Work Sans", Arial, sans-serif;
    color: var(--ink);
  }
  .stage {
    width: 1200px; height: 900px;
    display: flex; flex-direction: column;
    align-items: center; justify-content: center;
    gap: 44px;
  }
  .card {
    width: 660px; height: 377px;
    background: linear-gradient(135deg, var(--card-edge) 0%, var(--card) 55%, #1a1a1a 100%);
    box-shadow: 0 18px 40px rgba(0,0,0,0.6);
    position: relative;
  }
  .card--front { display: flex; align-items: center; justify-content: center; }
  .wordmark { display: flex; align-items: center; gap: 16px; }
  .wordmark__dot {
    width: 46px; height: 46px; border-radius: 50%;
    background: var(--ink); flex: none;
  }
  .wordmark__name {
    font-size: 24px; font-weight: 500; color: var(--ink);
    line-height: 1.2; letter-spacing: 0.02em;
  }

  .card--back { display: flex; align-items: center; padding: 0 0 0 50px; }
  .card--back .wordmark { width: 290px; }
  .divider {
    width: 1.5px; height: 196px; background: var(--ink-soft);
    margin: 0 32px 0 14px;
  }
  .contact { font-size: 15.5px; letter-spacing: 0.05em; color: var(--ink-soft); }
  .contact__name { font-size: 19px; font-weight: 600; letter-spacing: 0.09em; color: var(--ink); text-transform: uppercase; }
  .contact__role { font-size: 15px; margin-bottom: 18px; }
  .contact__address { line-height: 1.45; margin-bottom: 10px; }
  .contact__row { display: flex; align-items: center; gap: 12px; line-height: 1.9; }
  .contact__icon { width: 12px; height: 12px; flex: none; }
</style>
</head>
<body>
<main class="stage">
  <section class="card card--front">
    <div class="wordmark">
      <span class="wordmark__dot"></span>
      <span class="wordmark__name">Crimson Vantage<br>Cleaning Solutions</span>
    </div>
  </section>

  <section class="card card--back">
    <div class="wordmark">
      <span class="wordmark__dot"></span>
      <span class="wordmark__name">Crimson Vantage<br>Cleaning Solutions</span>
    </div>
    <div class="divider"></div>
    <div class="contact">
      <p class="contact__name">Rowan Hale</p>
      <p class="contact__role">Director</p>
      <p class="contact__address">218 Quarry Hollow Road<br>Alvin, TX 77511</p>
      <p class="contact__row">
        <svg class="contact__icon" viewBox="0 0 12 12" aria-hidden="true"><path d="M3 1 L5 3.5 L4 5 Q5 7 7 8 L8.5 7 L11 9 L9.5 11 Q5 11 2.5 7 Q1 4.5 1 2.5 Z" fill="none" stroke="#fff" stroke-width="1"/></svg>
        281-555-0147
      </p>
      <p class="contact__row">
        <svg class="contact__icon" viewBox="0 0 12 12" aria-hidden="true"><rect x="1" y="2.5" width="10" height="7" fill="none" stroke="#fff" stroke-width="1"/><path d="M1 2.5 L6 6.5 L11 2.5" fill="none" stroke="#fff" stroke-width="1"/></svg>
        info@crimsonvantage.com
      </p>
      <p class="contact__row">
        <svg class="contact__icon" viewBox="0 0 12 12" aria-hidden="true"><circle cx="6" cy="6" r="5" fill="none" stroke="#fff" stroke-width="1"/><ellipse cx="6" cy="6" rx="2.2" ry="5" fill="none" stroke="#fff" stroke-width="0.8"/><path d="M1 6 H11 M2 3.5 H10 M2 8.5 H10" stroke="#fff" stroke-width="0.7"/></svg>
        www.crimsonvantage.com
      </p>
    </div>
  </section>
</main>
</body>
</html>
```